Trifold brochure

Need a trifold marketing brochure for my autism therapy for children business . I would be interested in having designs in both English and Spanish if possible!!!!! Website is www.meadowlarkcareaba.com
Address on brochure needs to be 2718 Tamarind Ave W Suite 5
Minneapolis, MN 55192
Updates
Can you update the address on brochure to 2718 Tamarind Ave W Suite 5
Minneapolis, MN 55192
Target Market(s)
Autism therapy for children
Industry/Entity Type
Autism Therapy
Look and feel
Each slider illustrates characteristics of the customer's brand and the style your logo design should communicate.

```html
<!DOCTYPE html>
<html lang="en">
<head>
<meta charset="utf-8">
<title>Meadowlark Care – Trifold Brochure</title>
<link href="https://fonts.googleapis.com/css2?family=Montserrat:wght@300;400;600;700&display=swap" rel="stylesheet">
<style>
  :root{
    --blue:#1b5f98;
    --blue-deep:#174f80;
    --gold:#a56c2c;
    --amber:#e5a13d;
    --ink:#5b5b5b;
    --white:#ffffff;
    --stage:#dcdcdc;
  }
  *{margin:0;padding:0;box-sizing:border-box}
  html,body{width:863px;height:1200px;overflow:hidden;background:var(--stage)}
  body{font-family:"Montserrat",sans-serif;color:var(--ink)}
  .canvas{position:relative;width:863px;height:1200px;overflow:hidden;background:var(--stage)}

  .spread{position:absolute;left:95px;width:688px;height:487px;background:var(--white);
    box-shadow:0 10px 12px -6px rgba(0,0,0,.35);overflow:hidden}
  .spread--outside{top:90px}
  .spread--inside{top:617px}
  .spread-art{position:absolute;inset:0;width:688px;height:487px}

  .panel{position:absolute;top:0;height:487px}
  .panel--left{left:0;width:229px}
  .panel--middle{left:229px;width:229px}
  .panel--right{left:458px;width:230px}
  .fold-shade{position:absolute;inset:0;pointer-events:none}
  .fold-shade--left{background:linear-gradient(90deg,rgba(0,0,0,0) 75%,rgba(0,0,0,.06))}
  .fold-shade--right{background:linear-gradient(90deg,rgba(0,0,0,.06),rgba(0,0,0,0) 25%)}

  .photo{position:absolute}

  .service-title{position:absolute;font-weight:700;font-size:10px;color:var(--gold);letter-spacing:.1px}
  .body-copy{position:absolute;font-weight:300;font-size:8px;line-height:9.8px;text-align:justify;hyphens:auto;-webkit-hyphens:auto;color:var(--ink)}
  .body-copy--white{color:var(--white)}

  .contact-lead{position:absolute;left:27px;top:42px;width:190px;font-size:15.5px;line-height:17.6px;color:var(--white);font-weight:300}
  .contact-lead strong{color:var(--amber);font-weight:700}
  .map{position:absolute;left:17px;top:179px;width:193px;height:162px;border:3px solid #d8a455;border-radius:14px;
    background:linear-gradient(115deg,#9cc3ea 0%,#a9cdee 22%,#e9ebee 30%,#eef0f2 70%,#f3e7c6 100%)}
  .address{position:absolute;left:0;top:370px;width:229px;text-align:center;font-size:9.6px;line-height:12px;color:#444;font-weight:400}
  .phone{position:absolute;left:0;top:396px;width:229px;text-align:center;font-size:20px;font-weight:700;color:var(--gold)}
  .web-lines{position:absolute;left:0;top:420px;width:229px;text-align:center;font-size:9.6px;line-height:11.8px;color:#555}
  .social{position:absolute;left:70px;top:450px;display:flex;gap:3px}
  .social span{width:16px;height:16px;display:block}

  .brand{position:absolute;left:0;top:20px;width:230px;text-align:center}
  .brand-dot{width:22px;height:22px;border-radius:50%;background:var(--blue);margin:0 auto 8px}
  .brand-name{font-size:14.5px;font-weight:700;color:var(--blue);letter-spacing:.2px}
  .tagline{position:absolute;left:20px;top:418px;width:200px;font-weight:700;text-align:right;line-height:21px}
  .tagline-blue{display:block;color:var(--blue);font-size:18.5px}
  .tagline-gold{display:block;color:var(--gold);font-size:22px}

  .about-photo{left:0;top:0;width:229px;height:290px;
    background:linear-gradient(180deg,#d9c4a9 0%,#cdb49a 40%,#e9ddcf 75%,#ffffff 100%)}
  .about-title{position:absolute;left:22px;top:270px;font-size:13.5px;font-weight:700;color:var(--blue)}
  .call-line{position:absolute;left:33px;top:466px;font-size:11px;font-weight:700;color:var(--white)}

  .quality-title{position:absolute;left:9px;top:124px;font-size:11px;font-weight:700;color:var(--amber)}
  .value{position:absolute;left:14px;width:210px}
  .value-icon{position:absolute;left:0;top:0;width:22px;height:22px;border-radius:50%;background:var(--white)}
  .value-icon svg{display:block}
  .value-title{position:absolute;left:34px;top:-4px;font-size:10.5px;font-weight:700;color:var(--white)}
  .value .body-copy{left:34px;width:153px}
  .site-line{position:absolute;left:0;top:463px;width:229px;text-align:center;font-size:10px;font-weight:700;color:var(--white)}

  .services-title{position:absolute;left:23px;top:20px;font-size:13.5px;font-weight:700;color:var(--blue)}
  .cta{position:absolute;right:19px;text-align:right;font-weight:700;color:var(--white);font-size:11px;line-height:13.5px}
</style>
</head>
<body>
<div class="canvas">

  <section class="spread spread--outside">
    <svg class="spread-art" viewBox="0 0 688 487">
      <defs>
        <linearGradient id="warmPhoto" x1="0" y1="0" x2="1" y2="1">
          <stop offset="0" stop-color="#7c6a5a"/>
          <stop offset=".4" stop-color="#e8d58f"/>
          <stop offset=".75" stop-color="#d9c59a"/>
          <stop offset="1" stop-color="#c9a57a"/>
        </linearGradient>
      </defs>
      <rect width="688" height="487" fill="#fff"/>
      <path d="M229,0 H377 C405,35 430,60 458,79 V352 C410,344 300,318 229,272 Z" fill="var(--blue)"/>
      <g role="img" aria-label="Photo of a toddler in a yellow top playing with a colourful shape sorter while an adult guides her hand">
        <path d="M458,79 C530,125 620,135 688,107 V368 C620,384 530,380 458,360 Z" fill="url(#warmPhoto)"/>
      </g>
      <path d="M340,336 C370,352 400,360 440,366 C540,380 620,384 688,368 V378 C620,398 540,392 440,376 C400,370 370,360 340,336 Z" fill="var(--gold)"/>
    </svg>

    <div class="panel panel--left">
      <div class="photo" role="img" aria-label="Photo of a child moving beads on a colourful abacus"
           style="left:17px;top:29px;width:191px;height:94px;background:linear-gradient(90deg,#cdb6a8,#d9a0a8 45%,#e9c05a 75%,#d6c3b4)"></div>
      <div class="service-title" style="left:19px;top:137px">Occupational Therapy (OT)</div>
      <p class="body-copy" style="left:19px;top:151px;width:180px">Occupational therapy at Meadowlark Care targets the development of fine motor skills, sensory processing abilities, and self-care capabilities in children with autism.</p>
      <div class="photo" role="img" aria-label="Photo of a group of young children sitting around a table playing with blocks"
           style="left:17px;top:220px;width:191px;height:94px;background:linear-gradient(90deg,#b9bfb4,#8a7f6e 40%,#a7b39c 70%,#6d5c50)"></div>
      <div class="service-title" style="left:20px;top:326px">Social Skills Training</div>
      <p class="body-copy" style="left:20px;top:341px;width:180px">Our social skills training programs focus on teaching crucial social skills to children with autism, enabling them to navigate social interactions confidently. Through structured group activities and personalized coaching, we empower children to build friendships, communicate effectively, and thrive in social settings.</p>
      <div class="fold-shade fold-shade--left"></div>
    </div>

    <div class="panel panel--middle">
      <p class="contact-lead">Contact us today<br>to learn more about<br><strong>our ABA therapy for autism services and how we can help your child thrive.</strong></p>
      <div class="map" role="img" aria-label="Street map of the clinic neighbourhood with a location pin"></div>
      <p class="address">2718 Tamarind Ave W Suite 5<br>Minneapolis, MN 55192</p>
      <p class="phone">612-555-0148</p>
      <p class="web-lines">Info@meadowlarkcareaba.com<br>www.meadowlarkcareaba.com</p>
      <div class="social" aria-label="Social media links">
        <span style="background:#3a5a99"></span>
        <span style="background:#222"></span>
        <span style="background:#1f72b0"></span>
        <span style="background:#d22a2a"></span>
      </div>
    </div>

    <div class="panel panel--right">
      <div class="brand">
        <div class="brand-dot"></div>
        <div class="brand-name">MEADOWLARK CARE</div>
      </div>
      <h1 class="tagline"><span class="tagline-blue">Building Bridges to</span><span class="tagline-gold">Brighter Futures</span></h1>
      <div class="fold-shade fold-shade--right"></div>
    </div>
  </section>

  <section class="spread spread--inside">
    <svg class="spread-art" viewBox="0 0 688 487">
      <defs>
        <clipPath id="bandClip">
          <path d="M0,428 C130,468 320,472 458,430 C560,400 640,378 688,354 V487 H0 Z"/>
        </clipPath>
      </defs>
      <rect width="688" height="487" fill="#fff"/>
      <rect x="229" y="0" width="229" height="487" fill="var(--blue)"/>
      <path d="M0,428 C130,468 320,472 458,430 C560,400 640,378 688,354 V487 H0 Z" fill="var(--blue)"/>
      <rect x="229" y="0" width="229" height="487" fill="var(--gold)" clip-path="url(#bandClip)"/>
      <path d="M0,421 C130,461 320,465 458,423 C560,393 640,371 688,347" fill="none" stroke="var(--gold)" stroke-width="4"/>
    </svg>

    <div class="panel panel--left">
      <div class="photo about-photo" role="img" aria-label="Photo of a young boy playing with a wooden abacus beside a smiling therapist"></div>
      <h2 class="about-title">About ABA Therapy</h2>
      <p class="body-copy" style="left:22px;top:292px;width:179px">ABA Therapy Applied Behavioral Analysis (ABA) Therapy is endorsed by the Tamarind Child Health Board and the Northvale Pediatric Council and has been scientifically proven to be the most effective in helping a child with autism to acquire the necessary skills to reach their full potential. Research has proven that early diagnosis and intervention are key to achieving success, as well as a commitment to the individualized treatment plan developed specifically for your child by one of our expert Clinicians.</p>
      <p class="call-line">Call us : 612-555-0148</p>
    </div>

    <div class="panel panel--middle">
      <div class="photo" role="img" aria-label="Photo of a child's hands stacking colourful rings on a toy tower"
           style="left:8px;top:8px;width:214px;height:105px;background:linear-gradient(90deg,#8fa6c4,#e7c45a 35%,#6f8fbf 60%,#c7a283)"></div>
      <h2 class="quality-title">Quality Care From Quality Experts.</h2>
      <p class="body-copy body-copy--white" style="left:13px;top:144px;width:200px">At Meadowlark Care, our values drive our mission. We provide compassionate, evidence-based therapy for children with autism, focusing on individualized care and early intervention in a nurturing environment.</p>

      <div class="value" style="top:208px">
        <div class="value-icon"><svg width="22" height="22" viewBox="0 0 22 22"><circle cx="11" cy="11" r="5" fill="none" stroke="#c8323c" stroke-width="1.3"/><circle cx="11" cy="11" r="1.6" fill="#c8323c"/></svg></div>
        <h3 class="value-title">Vision</h3>
        <p class="body-copy body-copy--white" style="top:11px">To envision and strive towards a future where every child diagnosed with autism is supported, empowered, and equipped to achieve their fullest potential, fostering inclusivity and acceptance.</p>
      </div>
      <div class="value" style="top:291px">
        <div class="value-icon"><svg width="22" height="22" viewBox="0 0 22 22"><circle cx="11" cy="11" r="5" fill="#c8323c"/><path d="M13,9 L10,10 L9,13 L12,12 Z" fill="#fff"/></svg></div>
        <h3 class="value-title">Mission</h3>
        <p class="body-copy body-copy--white" style="top:11px">We're dedicated to providing person&shy;alized, evidence-based therapy for every child with autism. Through early intervention and compassionate care, we empower growth and confidence, fostering thriving futures.</p>
      </div>
      <div class="value" style="top:375px">
        <div class="value-icon"><svg width="22" height="22" viewBox="0 0 22 22"><rect x="7.5" y="7.5" width="7" height="7" rx="1" fill="#c8323c"/></svg></div>
        <h3 class="value-title">Motto</h3>
        <p class="body-copy body-copy--white" style="top:11px">Unlocking Potential, Building Bridges, Illuminating Futures: Together, We Build Brighter Tomorrows.</p>
      </div>
      <p class="site-line">www.meadowlarkcareaba.com</p>
    </div>

    <div class="panel panel--right">
      <h2 class="services-title">Our Services</h2>
      <div class="photo" role="img" aria-label="Photo of a boy practising speech sounds with a therapist against a blue wall"
           style="left:21px;top:45px;width:187px;height:94px;background:linear-gradient(90deg,#24558d,#3b6aa0 55%,#e8e6e4)"></div>
      <div class="service-title" style="left:22px;top:148px">ABA Therapy</div>
      <p class="body-copy" style="left:22px;top:161px;width:179px">Our ABA therapy focuses on enhancing communication, social skills, and behavior management in children with autism spectrum disorder (ASD).</p>
      <div class="photo" role="img" aria-label="Photo of a therapist and a young child sitting at a white table in a bright playroom"
           style="left:21px;top:215px;width:191px;height:94px;background:linear-gradient(90deg,#e8e4df,#c9b3a0 30%,#f1eeea 60%,#d8cfc5)"></div>
      <div class="service-title" style="left:27px;top:318px">Speech and Language Therapy</div>
      <p class="body-copy" style="left:27px;top:331px;width:175px">Our speech and language therapy services aim to improve communication, expressive language, and social interaction abilities in children with autism.</p>
      <p class="cta" style="top:411px">Ready to<br>Take &nbsp;the Next Step?</p>
      <p class="cta" style="top:446px">Contact Us Today for Expert<br>Autism Therapy Services!</p>
    </div>
  </section>

</div>
</body>
</html>
```